Letterhead to Prospective Clients

Create a letterhead (word & canva) that I will use to send letters to prospective clients and also include the Coralwood Estate Partners Logo, My Contact Details and Interchangeable "Suburb". Use the same font and colour pallete

Maris Dulworth | "Suburb" Specialist - Redlands & Surrounds
Mobile: 0417 862 095
Email: MD@CoralwoodEstatePartners.com.au

```html
<!DOCTYPE html>
<html lang="en">
<head>
<meta charset="UTF-8">
<title>Coralwood Estate Partners – Letterhead</title>
<link rel="stylesheet" href="https://fonts.googleapis.com/css2?family=Montserrat:wght@300;400;500&family=Roboto:wght@400;500;700&display=swap">
<style>
  :root {
    --navy: #23224f;
    --gold: #d9a86a;
    --text: #5a5a5a;
    --muted: #6b6b6b;
    --paper: #ffffff;
    --watermark: rgba(217, 168, 106, 0.18);
    --sign-area: #ececec;
  }
  * { margin: 0; padding: 0; box-sizing: border-box; }
  html, body { width: 900px; height: 1200px; overflow: hidden; background: var(--paper); }
  .letterhead {
    position: relative;
    width: 900px;
    height: 1200px;
    background: var(--paper);
    font-family: "Roboto", Arial, sans-serif;
    color: var(--text);
  }
  .side-accent { position: absolute; left: 0; top: 40px; width: 16px; height: 109px; background: var(--navy); }

  .brand-mark {
    position: absolute; left: 67px; top: 44px;
    font-family: "Montserrat", sans-serif; font-weight: 300; color: var(--gold);
    line-height: 1;
  }
  .brand-mark .line-top { display: block; font-size: 26px; letter-spacing: 3px; }
  .brand-mark .line-main { display: block; font-size: 62px; letter-spacing: 4px; margin-top: 2px; }

  .contact {
    position: absolute; left: 436px; top: 68px;
    font-family: "Montserrat", sans-serif; font-weight: 400; font-size: 13.5px;
    color: var(--navy); letter-spacing: 1.6px; text-transform: uppercase;
  }
  .contact li { list-style: none; height: 38px; }
  .contact .label { display: inline-block; width: 20px; }

  .header-rule { position: absolute; left: 68px; top: 164px; width: 762px; height: 3px; background: var(--navy); }

  .date {
    position: absolute; right: 70px; top: 209px;
    font-family: "Montserrat", sans-serif; font-weight: 300; font-size: 14px;
    letter-spacing: 1.5px; color: var(--muted);
  }

  .recipient { position: absolute; left: 104px; top: 220px; font-size: 13.5px; line-height: 24px; font-style: normal; }
  .recipient strong, .salutation strong, .closing { font-weight: 700; }
  .salutation { position: absolute; left: 104px; top: 333px; font-size: 13.5px; }

  .watermark {
    position: absolute; left: 0; width: 900px; text-align: center;
    font-family: "Montserrat", sans-serif; font-weight: 300; color: var(--watermark);
    line-height: 1; pointer-events: none;
  }
  .watermark.top { top: 500px; font-size: 62px; letter-spacing: 8px; }
  .watermark.main { top: 560px; font-size: 150px; letter-spacing: 12px; }

  .body-copy {
    position: absolute; left: 104px; top: 403px; width: 685px;
    font-size: 13.5px; line-height: 35.3px; text-align: justify; hyphens: auto;
  }
  .body-copy p + p { margin-top: 35px; }

  .closing { position: absolute; left: 104px; top: 896px; font-size: 13.5px; }
  .signature { position: absolute; left: 90px; top: 928px; width: 200px; height: 47px; background: var(--sign-area); border-radius: 4px; }
  .signatory {
    position: absolute; left: 97px; top: 990px;
    font-family: "Montserrat", sans-serif; font-weight: 300; font-size: 14px;
    letter-spacing: 4px; color: var(--muted);
  }

  .footer-mark {
    position: absolute; left: 73px; top: 1117px; width: 170px;
    font-family: "Montserrat", sans-serif; font-weight: 500;
    color: var(--navy); text-transform: uppercase; text-align: center; line-height: 1;
  }
  .footer-mark .name { display: block; font-size: 24px; letter-spacing: 1px; }
  .footer-mark .sub { display: block; font-size: 6.5px; letter-spacing: 2px; margin-top: 6px; }

  .tagline {
    position: absolute; right: 70px; top: 1130px;
    font-family: "Montserrat", sans-serif; font-weight: 400; font-size: 15px;
    letter-spacing: 1.6px; color: var(--navy); text-transform: uppercase; white-space: nowrap;
  }
  .tagline .suburb { background: var(--navy); color: var(--paper); padding: 2px 3px; margin-right: 2px; }

  .footer-band { position: absolute; left: 0; bottom: 0; width: 900px; height: 12px; display: flex; }
  .footer-band .navy { width: 272px; background: var(--navy); }
  .footer-band .gold { flex: 1; background: var(--gold); }
</style>
</head>
<body>
<main class="letterhead">
  <div class="side-accent"></div>

  <div class="brand-mark">
    <span class="line-top">CORALWOOD</span>
    <span class="line-main">MARIS</span>
  </div>

  <ul class="contact">
    <li><span class="label">M</span>: 0417 862 095</li>
    <li><span class="label">E</span>: MD@CoralwoodEstatePartners.com.au</li>
  </ul>

  <div class="header-rule"></div>

  <p class="date">JUNE 20, 2025</p>

  <address class="recipient">
    To<br>
    <strong>Client Name</strong><br>
    123 Address Here XX<br>
    XXXX, XXX
  </address>

  <p class="salutation">Dear <strong>Client Name</strong></p>

  <div class="watermark top" aria-hidden="true">CORALWOOD</div>
  <div class="watermark main" aria-hidden="true">MARIS</div>

  <div class="body-copy">
    <p>Lorem ipsum dolor sit amet, consectetur adipiscing elit, sed do eiusmod tempor incididunt ut labore et dolore magna aliqua. Nisl tincidunt eget nullam non. Quis hendrerit dolor magna eget est lorem ipsum dolor sit. Volutpat odio facilisis mauris sit amet massa. Commodo odio aenean sed adipiscing diam donec adipiscing tristique. Mi eget mauris pharetra et. Non tellus orci ac auctor augue. Elit at imperdiet dui accumsan sit. Ornare arcu dui vivamus arcu felis. Egestas integer eget aliquet nibh praesent. In hac habitasse platea dictumst quisque sagittis purus. Pulvinar elementum integer enim neque volutpat ac.</p>
    <p>Senectus et netus et malesuada. Nunc pulvinar sapien et ligula ullamcorper malesuada proin. Neque convallis a cras semper auctor. Libero id faucibus nisl tincidunt eget. Leo a diam sollicitudin tempor id. A lacus vestibulum sed arcu non odio euismod lacinia. In tellus integer feugiat scelerisque. Feugiat in fermentum posuere urna nec tincidunt praesent. Porttitor rhoncus dolor purus non enim praesent elementum facilisis. Nisi scelerisque eu ultrices vitae auctor eu augue ut lectus. Ipsum faucibus vitae aliquet nec ullamcorper sit amet risus. Et malesuada fames ac turpis egestas sed.</p>
  </div>

  <p class="closing">Kind Regards,</p>
  <div class="signature" role="img" aria-label="Handwritten signature of Maris Dulworth"></div>
  <p class="signatory">MARIS DULWORTH</p>

  <div class="footer-mark">
    <span class="name">Coralwood</span>
    <span class="sub">Estate Partners</span>
  </div>
  <p class="tagline"><span class="suburb">"SUBURB"</span> Specialist - Redlands &amp; Surrounds</p>

  <div class="footer-band"><span class="navy"></span><span class="gold"></span></div>
</main>
</body>
</html>
```